Website for Solar Renewable Company

We Driftwell Solar, are in need on a new website design. We design , manufacture and install floating solar plants. These plants are installed on reservoir , lakes and captive reservoir. We would like to build a professional website which shows the technical competency of our company as our product is highly technical .

Videos our projects
https://www.vidmora.example/watch?v=aQ3rT8LmZ2x
https://www.vidmora.example/watch?v=pB7nK2wXeR4&t=115s
https://www.vidmora.example/watch?v=mJ9_5QdTyHV&t=4s

Please see reference competitor websites
https://bormivane-plat.net/
https://en.tallmerenergy.com/
https://qx-hovrelt.com/

Tabs Needed
- About
- Team
- Solutions
- Projects
- News Update
- Contact

These are not certain - you can change the tabs if you want

Target Market(s)

Developer and EPC companies

Industry/Entity Type

Solar , Renewable Energy, Power

Coding

Coded - Design and coding required

Number of Pages Required

5+ page

Colors
0094D4
00A9DD
6FCCEA
C7EBF8
E9F6FB

Requirements
Nice to have
• Videos

```html
<!DOCTYPE html>
<html lang="en">
<head>
<meta charset="utf-8">
<title>Driftwell Solar – Floating Solar Plants</title>
<link rel="stylesheet" href="https://fonts.googleapis.com/css2?family=Roboto:wght@400;500;700&family=Poppins:wght@400;500;600&family=Open+Sans:wght@400;600;700&display=swap">
<style>
:root{
  --blue:#1467e6;
  --orange:#f4a21b;
  --ink:#1f1f1f;
  --text:#666;
  --light:#f4f4f4;
  --topbar:#232323;
  --footer:#2b2b2e;
  --white:#fff;
}
*{margin:0;padding:0;box-sizing:border-box}
html,body{width:1200px;height:4996px;overflow:hidden}
body{position:relative;font-family:"Roboto",Arial,sans-serif;color:var(--ink);background:var(--white)}
.abs{position:absolute}
a{color:inherit;text-decoration:none}

.topbar{left:0;top:0;width:1200px;height:47px;background:var(--topbar);color:#fff;font-size:12px}
.topbar .item{top:16px;display:flex;align-items:center;gap:8px}
.topbar .social{right:52px;top:17px;display:flex;gap:22px}
.dot-icon{width:12px;height:12px;border-radius:50%;background:var(--blue)}

.header{left:0;top:47px;width:1200px;height:106px;background:#fff;border-bottom:1px solid #e5e5e5}
.brand{font-weight:700;color:var(--blue);font-size:30px;letter-spacing:.5px;display:flex;align-items:center;gap:10px}
.brand .sq{width:14px;height:14px;background:var(--blue)}
.nav{left:417px;top:44px;font-size:12.5px;color:#333;font-weight:500}
.nav span{position:absolute;white-space:nowrap}
.btn-outline{border:2px solid var(--blue);color:var(--blue);font-weight:600;font-size:13px;display:flex;align-items:center;justify-content:center}
.btn{background:var(--blue);color:#fff;font-weight:600;font-size:13px;display:flex;align-items:center;justify-content:center}

.hero{left:0;top:153px;width:1200px;height:683px;background:linear-gradient(160deg,#3c6e7e 0%,#2d5f6a 40%,#27545e 60%,#2a5a4a 100%);overflow:hidden}
.hero-title{left:258px;top:104px;color:#fff;font-family:"Open Sans",sans-serif;font-size:52px;line-height:64px;font-weight:400}
.hero-title b{font-weight:700}
.hero-text{left:258px;top:250px;width:560px;color:#fff;font-size:13.5px;line-height:27px}
.hero-thumb{left:0;top:533px;width:275px;height:150px;background:linear-gradient(135deg,#3b5fa8,#2a4477)}
.play{border-radius:50%;display:flex;align-items:center;justify-content:center}
.hero-bar{left:275px;top:564px;width:925px;height:119px;background:rgba(25,35,40,.72);color:#fff;font-size:12px}

.map{left:150px;top:921px;width:470px;height:524px;background:radial-gradient(ellipse at 50% 45%,#d6e6fb 0%,#c7dcf8 60%,#fff 72%)}
.map-label{font-weight:700;font-size:14px;color:#222}
.eyebrow{color:var(--orange);font-weight:700;font-size:13px;letter-spacing:.3px}
.about-text{left:667px;width:420px;color:var(--text);font-size:13px;line-height:21px}

.services{left:0;top:1503px;width:1200px;height:1270px;background:var(--light)}
.sec-title{font-size:34px;font-weight:700;color:var(--ink);text-align:center;width:1200px;left:0}
.sec-title em{font-style:normal;color:var(--blue)}
.card{width:320px;height:436px}
.card .img{position:absolute;left:0;top:0;width:320px;height:370px}
.card .num{position:absolute;left:22px;top:298px;font-size:64px;font-weight:700;color:rgba(255,255,255,.55)}
.card .bar{position:absolute;left:0;top:370px;width:320px;height:66px;background:var(--blue);color:#fff;font-weight:700;font-size:18px;display:flex;align-items:center;justify-content:space-between;padding:0 28px;line-height:22px}

.vid-img{width:471px;height:343px}
.vid-card{width:355px;background:#fff;box-shadow:0 4px 18px rgba(0,0,0,.12);padding:44px 24px 20px}
.vid-card h4{color:var(--blue);font-family:"Poppins",sans-serif;font-weight:600;font-size:20px;line-height:26px}
.vid-card p{margin-top:14px;font-size:12px;line-height:20px;color:var(--text);font-family:"Poppins",sans-serif}
.vid-card .play{position:absolute;top:-26px;right:28px;width:80px;height:52px;background:var(--blue);border-radius:0}
.ring{width:34px;height:34px;border-radius:50%;background:#fff;display:flex;align-items:center;justify-content:center}
.vid-tag{background:rgba(60,60,60,.6);color:#fff;font-family:"Poppins",sans-serif;font-weight:600;font-size:22px;padding:2px 6px;line-height:26px}

.partner-cat{width:200px;text-align:center;font-weight:700;font-size:14px;top:4384px}
.partner-name{width:240px;text-align:center;font-size:30px;font-weight:700;color:#333;top:4462px}

.footer{left:0;top:4600px;width:1200px;height:396px;background:var(--footer);color:#a8a8ad;font-size:13px}
.footer h5{color:#fff;font-size:15px;font-weight:700}
.footer .col{line-height:26px}
</style>
</head>
<body>

<div class="abs topbar">
  <div class="abs item" style="left:56px">
    <svg width="14" height="16" viewBox="0 0 14 16"><path d="M7 0C3.7 0 1 2.6 1 5.9 1 10.3 7 16 7 16s6-5.7 6-10.1C13 2.6 10.3 0 7 0zm0 8.3a2.4 2.4 0 110-4.8 2.4 2.4 0 010 4.8z" fill="#fff"/></svg>
    <span>Suite # 12, Lotus Lane, Pune, India 41108</span>
  </div>
  <div class="abs item" style="left:384px">
    <svg width="15" height="15" viewBox="0 0 24 24"><path d="M6.6 10.8a15 15 0 006.6 6.6l2.2-2.2a1 1 0 011-.25 11.4 11.4 0 003.6.57 1 1 0 011 1V20a1 1 0 01-1 1A17 17 0 013 4a1 1 0 011-1h3.5a1 1 0 011 1c0 1.25.2 2.45.57 3.6a1 1 0 01-.25 1z" fill="#fff"/></svg>
    <span>+91 555 010 2040</span>
  </div>
  <div class="abs social"><i class="dot-icon"></i><i class="dot-icon"></i><i class="dot-icon"></i><i class="dot-icon"></i></div>
</div>

<header class="abs header">
  <div class="abs brand" style="left:54px;top:34px"><i class="sq"></i>Driftwell Solar</div>
  <nav class="abs nav">
    <span style="left:0">HOME</span>
    <span style="left:77px">ABOUT US</span>
    <span style="left:174px">TEAM</span>
    <span style="left:238px">SOLUTIONS</span>
    <span style="left:335px">PROJECTS</span>
    <span style="left:430px">NEWS</span>
    <span style="left:494px">CONTACT</span>
  </nav>
  <a class="abs btn-outline" style="left:1008px;top:29px;width:163px;height:48px">Get In Touch</a>
</header>

<section class="abs hero" role="img" aria-label="Aerial photo of a large floating solar plant on a reservoir">
  <h1 class="abs hero-title"><b>The Largest</b> manufacturer of<br>Floats in India</h1>
  <p class="abs hero-text">Driftwell has an in-house technical team for designing of mooring and anchoring. All mooring and anchoring design is vetted by third party. Current third party verification is done by Marine Register Bureau (MRB)</p>
  <a class="abs btn" style="left:258px;top:367px;width:165px;height:50px">Discover</a>
  <div class="abs hero-thumb" role="img" aria-label="Video thumbnail of floating solar panels">
    <div class="abs play" style="left:110px;top:50px;width:50px;height:50px;background:#222">
      <svg width="14" height="16" viewBox="0 0 14 16"><path d="M2 1l11 7-11 7z" fill="#fff"/></svg>
    </div>
  </div>
  <div class="abs hero-bar">
    <div class="abs" style="left:27px;top:40px">Phones</div>
    <div class="abs" style="left:27px;top:66px">+91 555 010 2040&nbsp;&nbsp;&nbsp;&nbsp;+91 555 010 2041</div>
    <div class="abs" style="left:305px;top:40px">Social</div>
    <div class="abs" style="left:305px;top:66px;display:flex;gap:24px"><i class="dot-icon" style="background:#fff"></i><i class="dot-icon" style="background:#fff"></i><i class="dot-icon" style="background:#fff"></i><i class="dot-icon" style="background:#fff"></i></div>
    <div class="abs" style="left:590px;top:58px;width:16px;height:16px;border:2px solid #fff;border-radius:50%;display:flex;align-items:center;justify-content:center"><i style="width:8px;height:8px;border-radius:50%;background:#fff"></i></div>
    <i class="abs" style="left:636px;top:62px;width:9px;height:9px;border-radius:50%;background:#fff"></i>
    <i class="abs" style="left:679px;top:62px;width:9px;height:9px;border-radius:50%;background:#fff"></i>
    <i class="abs" style="left:714px;top:66px;width:110px;height:1px;background:#bbb"></i>
    <div class="abs" style="left:843px;top:59px">1/3</div>
  </div>
</section>

<section class="about">
  <div class="abs map" role="img" aria-label="Map of India marking the manufacturing facilities"></div>
  <div class="abs map-label" style="left:350px;top:1010px">Sonipat, Haryana</div>
  <div class="abs map-label" style="left:92px;top:1110px;line-height:20px">Sanand,<br>Ahmedabad</div>
  <div class="abs map-label" style="left:270px;top:1155px;color:#2b3f7a;text-align:center;line-height:20px">MANUFACTURING<br>FACILITIES</div>
  <div class="abs map-label" style="left:385px;top:1307px">Ramagundam, Telengana</div>

  <div class="abs eyebrow" style="left:663px;top:927px">ABOUT US</div>
  <div class="abs" style="left:663px;top:962px;font-size:32px;font-weight:500">Welcome to the</div>
  <div class="abs" style="left:663px;top:1016px;font-size:48px;font-weight:700;color:var(--blue)">Driftwell Solar</div>
  <p class="abs about-text" style="top:1090px">Driftwell Solar was established in 2019 as a Subsidiary of Ravel Dayan Infrastructure Ltd. &amp; Tarvin Profiles Pvt. Ltd.</p>
  <p class="abs about-text" style="top:1172px">Ravel Dayan Infrastructure Ltd. has 3 decades of experience in plastic. A leading supplier in North India for Water Storage Tanks, Road Safety equipment and Solid Waste Management products.</p>
  <p class="abs about-text" style="top:1280px">Tarvin Profiles Pvt. Ltd. leading supplier of module mounting structures in India with an annual supply of more than 5GW.</p>
  <a class="abs btn" style="left:667px;top:1351px;width:167px;height:49px">Discover</a>
</section>

<section class="abs services">
  <div class="abs eyebrow" style="left:0;width:1200px;text-align:center;top:52px">WHAT WE DO?</div>
  <h2 class="abs sec-title" style="top:86px">Our <em>Services</em></h2>
  <p class="abs" style="left:110px;top:152px;width:980px;text-align:center;color:var(--text);font-size:14px;line-height:27px">Lorem Ipsum is simply dummy text of the printing and typesetting industry. Lorem Ipsum has been the industry's standard dummy text ever since the 1500s, when an unknown printer took a galley of type and scrambled it to make a type specimen book. It has survived not only five centuries, but also the leap into electronic typesetting, remaining essentially unchanged.</p>

  <div class="abs card" style="left:93px;top:260px">
    <div class="img" role="img" aria-label="Technical drawing of a float assembly with panel and aisle floats" style="background:linear-gradient(135deg,#e9eef2,#5b86c8 60%,#2f5fb0)"></div>
    <div class="num">01</div>
    <div class="bar">Designing<span>›</span></div>
  </div>
  <div class="abs card" style="left:440px;top:260px">
    <div class="img" role="img" aria-label="Floating solar array on green water" style="background:linear-gradient(160deg,#52b4b0,#2d8f95 55%,#2d5a8c)"></div>
    <div class="num">02</div>
    <div class="bar">Site Survey &amp; Analysis<span>›</span></div>
  </div>
  <div class="abs card" style="left:787px;top:260px">
    <div class="img" role="img" aria-label="Floats and crates stacked beside solar panels" style="background:linear-gradient(170deg,#a9a39a,#7a8aa0 45%,#2b4a8c)"></div>
    <div class="num">03</div>
    <div class="bar">Floater Supply<span>›</span></div>
  </div>
  <div class="abs card" style="left:93px;top:744px">
    <div class="img" role="img" aria-label="Workers installing floating solar panels" style="background:linear-gradient(170deg,#8fa8c4,#4c6b9a 50%,#2c4579)"></div>
    <div class="num">04</div>
    <div class="bar">Installation Supervision<span>›</span></div>
  </div>
  <div class="abs card" style="left:440px;top:744px">
    <div class="img" role="img" aria-label="Floating solar plant stretching across a reservoir" style="background:linear-gradient(175deg,#b7bec4,#6d7a86 45%,#3b4a58)"></div>
    <div class="num">05</div>
    <div class="bar">Mooring and Anchoring<br>Designing<span>›</span></div>
  </div>
  <div class="abs card" style="left:787px;top:744px">
    <div class="img" role="img" aria-label="Mooring and anchoring rig on a barge" style="background:linear-gradient(180deg,#6aa9e0,#4f7fb8 55%,#555)"></div>
    <div class="num">06</div>
    <div class="bar">Installation of<br>Mooring &amp; Anchoring<span>›</span></div>
  </div>
</section>

<section class="videos">
  <div class="abs eyebrow" style="left:120px;top:2870px">FROM OUR GALLERY</div>
  <h2 class="abs" style="left:120px;top:2898px;font-size:34px;font-weight:700">Latest <span style="color:var(--blue)">Videos</span></h2>
  <p class="abs" style="left:112px;top:2962px;width:480px;color:var(--text);font-size:13px;line-height:26px">Streamer fish California halibut Pacific saury. Slickhead grunion lake trout. Canthigaster rostrata spikefish brown trout loach</p>
  <a class="abs btn-outline" style="left:112px;top:3056px;width:123px;height:43px;font-size:13px">View all</a>

  <div class="abs vid-img" style="left:611px;top:2864px" role="img" aria-label="Video thumbnail of workers assembling floats on land">
    <div style="width:471px;height:343px;background:linear-gradient(160deg,#9aa6b0,#5d7497 45%,#2f4a86)"></div>
    <div class="abs vid-tag" style="left:0;top:8px;font-size:20px">Easy installation and assembly on land</div>
  </div>
  <div class="abs vid-card" style="left:638px;top:3114px;height:179px">
    <div class="abs play"><span class="ring"><svg width="12" height="14" viewBox="0 0 12 14"><path d="M1 1l10 6-10 6z" fill="#1467e6"/></svg></span></div>
    <h4>Central Grid Power Plant (CGPP)</h4>
    <p>100 Mw Floating Solar Project at Ramagundam<br>A Deadbloack casting site</p>
  </div>

  <div class="abs vid-img" style="left:114px;top:3157px" role="img" aria-label="Video thumbnail of a wide floating solar plant">
    <div style="width:471px;height:345px;background:linear-gradient(175deg,#8d95a0,#575f70 40%,#3b4254)"></div>
    <div class="abs vid-tag" style="left:4px;top:10px;line-height:24px">Capacity:<br><span style="font-weight:500;font-size:20px">3.65Mw DC x 6 Blocks</span></div>
  </div>
  <div class="abs vid-card" style="left:145px;top:3413px;height:174px">
    <div class="abs play"><span class="ring"><svg width="12" height="14" viewBox="0 0 12 14"><path d="M1 1l10 6-10 6z" fill="#1467e6"/></svg></span></div>
    <h4>India's Largest Commissioned FSPV Project</h4>
    <p>The project will annually save 46,000 Tons of CO2 emmisions and 1,364 million liters of water.</p>
  </div>

  <div class="abs vid-img" style="left:611px;top:3364px" role="img" aria-label="Video thumbnail of a floating PV plant near a power station">
    <div style="width:471px;height:342px;background:linear-gradient(175deg,#9fc3d8,#5f88b8 45%,#2f4f96)"></div>
  </div>
  <div class="abs vid-card" style="left:638px;top:3612px;height:181px">
    <div class="abs play"><span class="ring"><svg width="12" height="14" viewBox="0 0 12 14"><path d="M1 1l10 6-10 6z" fill="#1467e6"/></svg></span></div>
    <h4>CGPP Varunpet, Vishakapatnam, India</h4>
    <p>21 Mw Floating PV Plant at CGPP Varunpet, Vishakapatnam, India</p>
  </div>
</section>

<section class="testimonials">
  <div class="abs" style="left:93px;top:3884px;width:177px;height:343px;background:linear-gradient(170deg,#8a8c90,#55585e)" role="img" aria-label="Portrait of a smiling client"></div>
  <div class="abs" style="left:242px;top:3926px;width:55px;height:103px;background:var(--blue);color:#fff;font-size:44px;font-weight:700;display:flex;align-items:center;justify-content:center;font-family:Georgia,serif">“</div>
  <div class="abs eyebrow" style="left:355px;top:3890px">TESTIMONIALS</div>
  <h2 class="abs" style="left:355px;top:3918px;font-size:34px;font-weight:700">People <span style="color:var(--blue)">Says</span></h2>
  <p class="abs" style="left:355px;top:3978px;width:740px;color:var(--text);font-size:16px;line-height:27px">Slickhead grunion lake trout. Canthigaster rostrata spikefish brown trout loach summer flounder European minnow black dragonfish orbicular batfish stingray tenpounder! Flying characin herring, Moses sole sea snail grouper discus. European eel slender snipe eel. Gulper eel dealfish ocean sunfish; rohu yellow-and-black triplefin Atlantic saury swordfish"</p>
  <div class="abs" style="left:355px;top:4140px;display:flex;align-items:center;gap:18px;font-size:13px;font-weight:500">
    <i style="width:36px;height:1px;background:var(--blue)"></i><span>Arun Mehlor, <span style="color:var(--blue)">CEO Brightvane Systems LLC</span></span>
  </div>
  <div class="abs" style="left:907px;top:3915px;width:17px;height:17px;border:2px solid var(--blue);border-radius:50%;display:flex;align-items:center;justify-content:center"><i style="width:8px;height:8px;border-radius:50%;background:var(--blue)"></i></div>
  <i class="abs" style="left:954px;top:3920px;width:8px;height:8px;border-radius:50%;background:#bbb"></i>
  <i class="abs" style="left:997px;top:3920px;width:8px;height:8px;border-radius:50%;background:#bbb"></i>
</section>

<section class="partners">
  <div class="abs eyebrow" style="left:0;width:1200px;text-align:center;top:4271px">MATERIAL PROVIDERS</div>
  <h2 class="abs sec-title" style="top:4300px">Our <em>Partners</em></h2>
  <div class="abs partner-cat" style="left:96px">POLYMERS</div>
  <div class="abs partner-cat" style="left:367px">POLYMERS</div>
  <div class="abs partner-cat" style="left:602px">POLYMERS</div>
  <div class="abs partner-cat" style="left:866px">ADDITIVES</div>
  <div class="abs partner-name" style="left:76px">Brelmontix</div>
  <div class="abs partner-name" style="left:347px;top:4450px;line-height:30px">Varnholt<br><span style="font-size:15px">Industries Limited</span></div>
  <div class="abs partner-name" style="left:582px">Tesselind</div>
  <div class="abs partner-name" style="left:846px">Calvquor</div>
</section>

<footer class="abs footer">
  <div class="abs brand" style="left:97px;top:86px;color:#fff;font-size:28px">Driftwell Solar</div>
  <div class="abs" style="left:112px;top:158px;display:flex;gap:16px"><i class="dot-icon" style="width:10px;height:10px;background:#888"></i><i class="dot-icon" style="width:10px;height:10px;background:#888"></i><i class="dot-icon" style="width:10px;height:10px;background:#888"></i><i class="dot-icon" style="width:10px;height:10px;background:#888"></i></div>

  <h5 class="abs" style="left:355px;top:80px">Contacts</h5>
  <div class="abs col" style="left:355px;top:116px">Harlow Ave, Fernvale 3052,<br>Melbourne Canada<br>Phone: +31 55 010 47 25<br>Email: hello@driftwell.example</div>

  <h5 class="abs" style="left:609px;top:80px">Company and Links</h5>
  <div class="abs col" style="left:609px;top:116px;color:#e4e4e4">Home<br>About Us<br>Services<br>Case studios</div>
  <div class="abs col" style="left:727px;top:116px;color:#e4e4e4">Shop<br>Blog<br>Elements<br>Contacts</div>

  <h5 class="abs" style="left:863px;top:80px">Information for Download</h5>
  <div class="abs" style="left:863px;top:118px;width:240px;line-height:22px">Direct link for downloading the file which you can use</div>
  <a class="abs btn" style="left:863px;top:174px;width:236px;height:41px">Download PDF</a>

  <div class="abs" style="left:102px;top:346px;font-size:11px">Copyright 2022 Driftwell. All rights reserved.</div>
  <div class="abs" style="left:886px;top:346px;font-size:11px"><u>Privacy Policy</u>&nbsp;&nbsp;|&nbsp;&nbsp;<u>Term and Condision</u></div>
</footer>

</body>
</html>
```